Kestrel Calisthenics Gym Website

We need a website design for our gym.

Kestrel is the UAE's first calisthenics and parkour gym. The theme under which the gym revolves is that one does not require any machinery to workout as our bodies could be themselves the machinery. The gym is designed to be the more of a social hub rather than an "in-and-out" gym, where people come train, have fun, hang out and socialize for a few hours rather than just train for 60 minutes then leave. The gym is designed to be a big open space with lots of natural sunlight, natural wood and plants all over the place to create a natural and refreshing setting. We also use recycled material throughout the gym and recycle our waste as being green is part of our philosophy. We currently also have some of the world's top and most recognized calisthenics athletes working with us.

We would like our website to reflect all that as well as provide a simple, interactive and fun way for visitors to be able to get class and gym information, check out gym media and contact us for bookings.

Target Market(s)

Ages 15-35

Industry/Entity Type

Fitness

Coding

Coded - Design and coding required

Number of Pages Required

4 page

Font styles to use
Decorative

Colors
0792cd

Requirements
Must have
• Class descriptions
• Gym description
• Class schedules
• Trainer profiles
• Gym philosophy
• Contact Details
Nice to have
• A link to contact us directly for a free first trial class

```html
<!DOCTYPE html>
<html lang="en">
<head>
<meta charset="utf-8">
<title>Kestrel Calisthenics Gym</title>
<link rel="stylesheet" href="https://fonts.googleapis.com/css2?family=Rubik:ital,wght@1,800;1,900&family=Ubuntu:ital,wght@0,400;0,500;1,700&display=swap">
<style>
:root{
  --brand:#0792cd;
  --brand-dark:#0a7aa8;
  --page-dark:#2b3035;
  --card:#1a1e22;
  --footer:#050708;
  --text-light:#e6e9ec;
  --text-muted:#b5bcc3;
  --white:#ffffff;
}
*{margin:0;padding:0;box-sizing:border-box}
html,body{width:1062px;height:1200px;overflow:hidden}
body{position:relative;background:var(--page-dark);font-family:"Ubuntu",sans-serif;color:var(--text-light)}
.abs{position:absolute}
.heading{font-family:"Rubik",sans-serif;font-style:italic;font-weight:900;color:var(--white)}

.main-nav{left:0;top:0;width:1062px;height:46px;background:linear-gradient(#2b2f33,#16191c);display:flex;align-items:center;padding-left:125px}
.main-nav a{color:var(--white);text-decoration:none;font-size:11px;text-transform:uppercase;white-space:nowrap}
.main-nav a.active{color:var(--brand)}
.main-nav .sep{width:14px;height:10px;margin:0 14px}

.top-band{left:0;top:46px;width:1062px;height:338px;background:var(--white)}
.lower-band{left:0;top:434px;width:1062px;height:328px;background:linear-gradient(#2e3338,#25292d)}

.phone-badge{left:98px;top:62px;width:30px;height:30px;border-radius:50%;background:var(--brand-dark)}
.phone-number{left:136px;top:68px;font-family:"Rubik",sans-serif;font-style:italic;font-weight:800;font-size:13px;color:#222}
.social{top:64px;width:26px;height:26px;border-radius:50%;background:var(--brand-dark)}

.hero-photo{left:98px;top:106px;width:866px;height:425px;border-radius:4px;
  background:
   radial-gradient(ellipse 22% 45% at 50% 40%,rgba(190,150,120,.55),transparent 70%),
   radial-gradient(ellipse 30% 50% at 85% 35%,rgba(60,110,170,.55),transparent 70%),
   radial-gradient(ellipse 30% 40% at 22% 30%,rgba(150,110,70,.6),transparent 70%),
   linear-gradient(180deg,#3b3a35 0%,#2f3a44 60%,#1f2327 100%)}
.logo-box{left:458px;top:56px;width:148px;height:102px;background:var(--white);box-shadow:0 2px 6px rgba(0,0,0,.3);display:flex;align-items:center;justify-content:center;gap:6px}
.logo-box .dot{width:12px;height:12px;border-radius:50%;background:var(--brand)}
.logo-box .name{font-weight:500;font-size:24px;color:#222}

.hero-band-side{top:384px;height:50px;background:rgba(7,146,205,.92)}
.hero-band-mid{left:372px;top:384px;width:317px;height:50px;background:rgba(7,146,205,.25)}
.hero-title{left:330px;top:374px;width:400px;text-align:center;font-size:27px;font-weight:800;line-height:37px;text-shadow:0 2px 4px rgba(0,0,0,.4)}
.cta{left:394px;top:502px;width:274px;height:56px;background:linear-gradient(#0a9fd8,#0782b6);border-radius:2px;display:flex;align-items:center;justify-content:center;color:var(--white);font-size:18px;font-weight:500;letter-spacing:.8px;text-decoration:none}

.card{top:586px;width:422px;height:140px;background:var(--card);border-radius:3px}
.card-photo{top:16px;left:15px;width:158px;height:108px}
.tag{background:#2a2f34;border-radius:2px;height:31px;display:flex;align-items:center;padding:0 13px;font-size:11.5px;font-weight:800}
.card-text{font-size:10.5px;line-height:23px;color:var(--text-muted);text-align:justify}
.time{color:var(--brand);font-size:11px;font-weight:500}
.mini-arrow{width:12px;height:12px;border-radius:50%;background:#9aa1a8}

.trainers-band{left:0;top:762px;width:1062px;height:244px;
  background:radial-gradient(ellipse 40% 60% at 30% 30%,rgba(70,74,78,.7),transparent 70%),linear-gradient(90deg,#2c2f32,#222528 50%,#2e3032)}
.trainers-box{left:98px;top:800px;width:160px;height:170px;background:linear-gradient(#0a9fd8,#077fae);border-radius:2px}
.trainers-box .heading{position:absolute;left:27px;top:32px;font-size:18px;font-weight:800;line-height:22px}
.ring{width:22px;height:22px}
.trainer-panel{left:274px;top:800px;width:690px;height:170px;background:rgba(20,24,28,.88);border-radius:3px}
.trainer-photo{left:17px;top:16px;width:192px;height:138px;
  background:radial-gradient(ellipse 40% 60% at 65% 60%,rgba(60,80,90,.6),transparent 70%),linear-gradient(180deg,#e8ecee 0%,#b9c1c6 55%,#3a3f44 100%)}
.trainer-name{left:230px;top:27px;font-size:16px;font-weight:800}
.trainer-bio{left:230px;top:62px;width:440px;font-size:10.5px;line-height:23px;color:var(--text-muted)}
.small-social{top:25px;width:22px;height:22px;border-radius:50%;background:var(--brand-dark)}

.site-footer{left:0;top:1006px;width:1062px;height:194px;background:var(--footer)}
.foot-name{left:98px;top:1050px;display:flex;align-items:center;gap:6px;font-size:20px;font-weight:500;color:#9a9fa4}
.foot-name .dot{width:9px;height:9px;border-radius:50%;background:#9a9fa4}
.copyright{left:98px;top:1117px;font-size:11px;line-height:18px;color:#b0b5ba}
.divider{top:1038px;width:1px;height:134px;background:#1e2226}
.foot-heading{top:1036px;font-size:16px;font-weight:800}
.foot-link{font-size:11px;color:#b0b5ba}
.contact-item{left:690px;font-size:11px;color:#b0b5ba;display:flex;align-items:center;gap:6px}
.contact-item svg{width:13px;height:13px}
</style>
</head>
<body>

<nav class="abs main-nav">
  <a class="active" href="#">Home</a>
  <svg class="sep" viewBox="0 0 14 10"><circle cx="3" cy="3" r="1.6" fill="#888"/><circle cx="10" cy="5" r="1.6" fill="#888"/><circle cx="5" cy="8" r="1.6" fill="#888"/></svg>
  <a href="#">Class Descriptions</a>
  <svg class="sep" viewBox="0 0 14 10"><circle cx="3" cy="3" r="1.6" fill="#888"/><circle cx="10" cy="5" r="1.6" fill="#888"/><circle cx="5" cy="8" r="1.6" fill="#888"/></svg>
  <a href="#">Gym Description</a>
  <svg class="sep" viewBox="0 0 14 10"><circle cx="3" cy="3" r="1.6" fill="#888"/><circle cx="10" cy="5" r="1.6" fill="#888"/><circle cx="5" cy="8" r="1.6" fill="#888"/></svg>
  <a href="#">Class Schedules</a>
  <svg class="sep" viewBox="0 0 14 10"><circle cx="3" cy="3" r="1.6" fill="#888"/><circle cx="10" cy="5" r="1.6" fill="#888"/><circle cx="5" cy="8" r="1.6" fill="#888"/></svg>
  <a href="#">Trainer Profiles</a>
  <svg class="sep" viewBox="0 0 14 10"><circle cx="3" cy="3" r="1.6" fill="#888"/><circle cx="10" cy="5" r="1.6" fill="#888"/><circle cx="5" cy="8" r="1.6" fill="#888"/></svg>
  <a href="#">Gym Philosophy</a>
  <svg class="sep" viewBox="0 0 14 10"><circle cx="3" cy="3" r="1.6" fill="#888"/><circle cx="10" cy="5" r="1.6" fill="#888"/><circle cx="5" cy="8" r="1.6" fill="#888"/></svg>
  <a href="#">Contact</a>
</nav>

<div class="abs top-band"></div>
<div class="abs lower-band"></div>

<div class="abs phone-badge">
  <svg viewBox="0 0 30 30" width="30" height="30"><path d="M11 9c1 0 2 2.5 2 3s-1 1-1 1.5c.5 1.5 2.5 3.5 4 4 .5 0 1-1 1.5-1s3 1 3 2-1.5 2.5-3 2.5C13 21 9 17 9 12c0-1.5 1-3 2-3z" fill="#fff"/></svg>
</div>
<div class="abs phone-number">123 456 789 000</div>
<div class="abs social" style="left:880px"></div>
<div class="abs social" style="left:909px"></div>
<div class="abs social" style="left:938px"></div>

<div class="abs hero-photo" role="img" aria-label="Athlete performing a bar move inside the gym, with racks, rings and plants"></div>
<div class="abs hero-band-side" style="left:0;width:372px"></div>
<div class="abs hero-band-side" style="left:689px;width:373px"></div>
<div class="abs hero-band-mid"></div>
<svg class="abs" style="left:336px;top:399px" width="22" height="18" viewBox="0 0 22 18"><path d="M20 9H3M10 2L3 9l7 7" stroke="#fff" stroke-width="2.6" fill="none"/></svg>
<svg class="abs" style="left:706px;top:399px" width="22" height="18" viewBox="0 0 22 18"><path d="M2 9h17M12 2l7 7-7 7" stroke="#fff" stroke-width="2.6" fill="none"/></svg>
<h1 class="abs heading hero-title">CALISTHENICS AND<br>PARKOUR GYM</h1>
<svg class="abs" style="left:520px;top:456px" width="20" height="32" viewBox="0 0 20 32"><path d="M10 0v28M2 20l8 9 8-9" stroke="#c8cdd2" stroke-width="2.4" fill="none"/></svg>
<a class="abs cta" href="#">FREE FIRST TRIAL CLASS</a>

<div class="abs logo-box"><span class="dot"></span><span class="name">Kestrel</span></div>

<section class="abs card" style="left:98px">
  <div class="abs card-photo" role="img" aria-label="Trainer coaching a member lifting dumbbells" style="background:radial-gradient(ellipse 50% 50% at 40% 45%,rgba(150,110,90,.5),transparent 70%),linear-gradient(180deg,#8a8d90 0%,#c6c8ca 55%,#2e3134 100%)"></div>
  <div class="abs tag heading" style="left:189px;top:16px">ABOUT THE GYM</div>
  <p class="abs card-text" style="left:189px;top:55px;width:218px">Lorem ipsum dolor sit amet, consectetur adipis cing elit. Proin eget ante mauris. Curabitur conva llis justo ex, sed vehicula...</p>
</section>

<section class="abs card" style="left:542px">
  <div class="abs card-photo" role="img" aria-label="Gymnastic ring hanging from a blue rig" style="background:radial-gradient(ellipse 25% 35% at 65% 70%,rgba(190,150,110,.6),transparent 70%),linear-gradient(135deg,#2a6fa8 0%,#dfe6ea 50%,#3a6d8f 100%)"></div>
  <div class="abs tag heading" style="left:190px;top:16px">CLASS SCHEDULES</div>
  <span class="abs mini-arrow" style="left:343px;top:26px"></span>
  <span class="abs mini-arrow" style="left:358px;top:26px"></span>
  <div class="abs time" style="left:190px;top:60px">6 AM TO 8AM</div>
  <p class="abs card-text" style="left:190px;top:78px;width:218px">Nam malesuada sit amet libero ac euismod. Fusce vulputate est vestibulum dolor.</p>
</section>

<div class="abs trainers-band" role="img" aria-label="Dim view of the gym's climbing rig and equipment"></div>
<div class="abs trainers-box">
  <h2 class="heading">OUR<br>TRAINERS</h2>
  <svg class="abs ring" style="left:27px;top:87px" viewBox="0 0 22 22"><circle cx="11" cy="11" r="9.5" stroke="#fff" stroke-width="2" fill="none"/><path d="M16 11H6M10 7l-4 4 4 4" stroke="#fff" stroke-width="2" fill="none"/></svg>
  <svg class="abs ring" style="left:57px;top:87px" viewBox="0 0 22 22"><circle cx="11" cy="11" r="9.5" stroke="#fff" stroke-width="2" fill="none"/><path d="M6 11h10M12 7l4 4-4 4" stroke="#fff" stroke-width="2" fill="none"/></svg>
</div>
<section class="abs trainer-panel">
  <div class="abs trainer-photo" role="img" aria-label="Trainers talking beside the rope net and climbing frame"></div>
  <h3 class="abs heading trainer-name">SAM ROWE</h3>
  <span class="abs small-social" style="left:632px"></span>
  <span class="abs small-social" style="left:657px"></span>
  <p class="abs trainer-bio">Sed ultricies ligula vitae metus bibendum iaculis egestas et quam. Interdum et malesuada fames ac ante ipsum primis in faucibus. Vestibulum dolor lorem, finibus a libero id, dignissim malesuada magna. Donec vehicula tellus orci, et pulvinar quam malesuada at. Vivamus diam magna, feugiat at justo sollicitudin, pharetra tempus velit...</p>
</section>

<footer class="abs site-footer"></footer>
<div class="abs foot-name"><span class="dot"></span>Kestrel</div>
<p class="abs copyright">Copyrights @ 2015 Kestrel.<br>All Right Reserved.</p>
<div class="abs divider" style="left:294px"></div>
<div class="abs divider" style="left:622px"></div>

<h4 class="abs heading foot-heading" style="left:352px">QUICK LINKS</h4>
<a class="abs foot-link" style="left:352px;top:1066px">Class descriptions</a>
<a class="abs foot-link" style="left:352px;top:1093px">Gym description</a>
<a class="abs foot-link" style="left:352px;top:1120px">Class schedules</a>
<a class="abs foot-link" style="left:352px;top:1147px">Trainer profiles</a>
<a class="abs foot-link" style="left:489px;top:1066px">Gym philosophy</a>
<a class="abs foot-link" style="left:489px;top:1093px">Contact</a>
<a class="abs foot-link" style="left:489px;top:1120px">Privacy Policy</a>
<a class="abs foot-link" style="left:489px;top:1147px">Sitemap</a>

<h4 class="abs heading foot-heading" style="left:690px">GET IN TOUCH</h4>
<div class="abs contact-item" style="top:1070px"><svg viewBox="0 0 13 13"><path d="M6.5 1a4 4 0 0 1 4 4c0 3-4 7-4 7s-4-4-4-7a4 4 0 0 1 4-4z" fill="#0792cd"/><circle cx="6.5" cy="5" r="1.5" fill="#050708"/></svg>123 Lorem Ipsm..., Lorem Ipsm - 123 456</div>
<div class="abs contact-item" style="top:1100px"><svg viewBox="0 0 13 13"><rect x="0.5" y="2.5" width="12" height="8" fill="#0792cd"/><path d="M1 3l5.5 4L12 3" stroke="#050708" fill="none"/></svg>info@domainname.com</div>
<div class="abs contact-item" style="top:1127px"><svg viewBox="0 0 13 13"><rect x="0.5" y="0.5" width="12" height="12" rx="2" fill="#0792cd"/><path d="M4 3c.7 0 1.2 1.5 1.2 2s-.6.5-.6.9c.3.9 1.5 2 2.4 2.4.4 0 .6-.6.9-.6s1.8.5 1.8 1.1-.9 1.5-1.8 1.5C5 10.3 3 8 3 5c0-1 .5-2 1-2z" fill="#050708"/></svg>+41 123 456 789 000</div>
<div class="abs contact-item" style="top:1156px"><svg viewBox="0 0 13 13"><rect x="0.5" y="3" width="12" height="9.5" rx="1" fill="#0792cd"/><rect x="3" y="0.5" width="7" height="4" fill="#0792cd"/><rect x="3" y="6" width="7" height="1.4" fill="#050708"/><rect x="3" y="8.6" width="7" height="1.4" fill="#050708"/></svg>+41 123 456 789 000</div>

</body>
</html>
```